Brivolta ERP Campaign Newsletter

Purpose of Document: Professional consulting firm looking to provide prospects with information about our ERP offerings and how we can support them with their ERP implementations. Often we have prospects that are in the middle of implementation and decide they need support.
What are we looking for: Professional look. Please use the attached ERP V5 document brochure content. We are looking for new graphics and layout that makes the content pop. Below is our website and attached company color skus. We want to keep our theme/colors consistent with the website.
Website: https://brivoltaconsulting.example/

Target Market(s)

Target prospects in industries including manufacturing and distribution, supply chain and logistics, and professional services.

Industry/Entity Type

Consulting

Requirements
Must have
• Visual graphics

```html
<!DOCTYPE html>
<html lang="en">
<head>
<meta charset="utf-8">
<title>Brivolta ERP Newsletter</title>
<link href="https://fonts.googleapis.com/css2?family=Inter:wght@400;500;600;700;800&display=swap" rel="stylesheet">
<style>
:root{
  --navy-deep:#0f2238;
  --navy:#153a63;
  --navy-dark:#0e2846;
  --blue:#2b5d8f;
  --blue-text:#1b4f86;
  --yellow:#f2c31b;
  --gray-text:#7a7a7a;
  --band:#e9eef5;
  --white:#ffffff;
}
*{margin:0;padding:0;box-sizing:border-box}
html,body{width:1200px;height:2956px;overflow:hidden;background:var(--white);font-family:'Inter',sans-serif}
.page{position:relative;width:1200px;height:2956px}
.abs{position:absolute}
.masthead{left:0;top:0;width:1200px;height:144px;background:var(--navy-deep);display:flex;align-items:center;justify-content:center}
.brand{color:#d4d8de;font-size:78px;font-weight:500;letter-spacing:1px}
.hero{left:0;top:144px;width:1200px;height:534px;background:radial-gradient(ellipse at 70% 80%,#2a6aa8 0%,#174a80 45%,#0f2f55 100%)}
.section-title{left:0;width:1200px;text-align:center;font-weight:700;font-size:43px;letter-spacing:.5px}
.rule{left:560px;width:80px;height:4px;background:var(--yellow)}
.hero-copy{left:410px;top:312px;width:755px;color:var(--white);font-size:20.5px;line-height:35px}
.hero-copy p+p{margin-top:20px}
.card{top:847px;height:453px;color:var(--white);padding:98px 38px 0 38px}
.card h3{font-size:30px;font-weight:700;line-height:40px;margin-bottom:20px}
.card .desc{font-size:17.5px;line-height:24px;margin-bottom:28px}
.card ul{list-style:none;font-size:15px;line-height:21.5px}
.card li{padding-left:16px;position:relative}
.card li::before{content:"›";position:absolute;left:0;top:-2px;color:var(--yellow);font-weight:700;font-size:20px}
.badge{width:100px;height:100px;border-radius:50%;background:var(--yellow);top:812px}
.value-title{left:0;top:1358px;width:1200px;text-align:center;color:var(--navy-deep);font-size:38px;font-weight:700}
.spine{left:118px;top:1540px;width:3px;height:660px;background:var(--blue-text)}
.node{left:57px;width:126px;height:126px;border-radius:50%;border:3px solid var(--blue-text);background:var(--white)}
.node::after{content:"";position:absolute;inset:9px;border:2px solid var(--blue-text);border-radius:50%}
.node svg{position:absolute;left:33px;top:33px}
.value-item{left:218px;width:920px}
.value-item h4{color:var(--blue-text);font-size:29px;font-weight:700;margin-bottom:10px}
.value-item p{color:var(--gray-text);font-size:20.5px;line-height:27px}
.platforms{left:0;top:2339px;width:1200px;height:177px;background:var(--band)}
.platforms-label{left:82px;top:2410px;font-size:43px;font-weight:700;color:var(--navy-deep)}
.partner{font-size:34px;color:var(--navy-deep);font-weight:400;line-height:40px}
.offer-title{left:286px;top:2550px;font-size:24px;font-weight:700;color:var(--blue-text)}
.offer-list{font-size:24px;color:var(--blue-text);line-height:40px;list-style:none}
.offer-list li::before{content:"• "}
.contact{left:0;top:2706px;width:1200px;height:164px;background:var(--blue)}
.contact-text{color:var(--white);font-size:24px;line-height:34px}
.copyright{left:0;top:2903px;width:1200px;text-align:center;color:var(--gray-text);font-size:20px}
</style>
</head>
<body>
<div class="page">
  <header class="abs masthead"><span class="brand">Brivolta</span></header>

  <section class="abs hero" role="img" aria-label="Blue digital network background"></section>
  <h1 class="abs section-title" style="top:192px;color:var(--white)">OUR ERP APPROACH</h1>
  <div class="abs rule" style="top:248px"></div>
  <div class="abs hero-copy">
    <p>Our approach is to give you what you need to get the most from your ERP implementation. If you know what that is, we can leverage a resource base of over 200 ERP consultants, both onshore and off, to provide the expertise that will fit seamlessly into your team.</p>
    <p>If you don’t know what you need, we have a process to help you figure that out.&nbsp; Our eight-point assessment starts with strategy and covers the other seven essential elements that ensure implementation success.</p>
  </div>

  <h2 class="abs section-title" style="top:724px;color:var(--navy-deep)">OUR ERP SERVICES</h2>
  <div class="abs rule" style="top:779px"></div>

  <article class="abs card" style="left:0;width:394px;background:var(--blue)">
    <h3>ERP<br>Implementations</h3>
    <p class="desc">Select and implement the right ERP platform for your needs and objectives</p>
    <ul><li>Start to Finish Implementations</li><li>Project Turnarounds</li><li>Hard to Find Resources</li><li>Value Add Solutions</li></ul>
  </article>
  <article class="abs card" style="left:403px;width:394px;background:var(--navy)">
    <h3>ERP Leadership<br>&amp; Staffing</h3>
    <p class="desc">Secure top match talent from interim CIOs to software engineers and project managers</p>
    <ul><li>Strategy Focused Leadership and Expertise</li><li>Right-sized for Your Business</li><li>Maximize ROI</li><li>Lead from Experience</li></ul>
  </article>
  <article class="abs card" style="left:806px;width:394px;background:var(--navy-dark)">
    <h3>ERP Transformation<br>&amp;&nbsp; Strategy</h3>
    <p class="desc">Define and execute your transformation strategy and clarify technologies to make it real.</p>
    <ul><li>Strategy and Innovation</li><li>Digital and Technology Prioritization &amp; Roadmap</li><li>Executive Coaching</li><li>Process Adoption &amp; Optimization</li></ul>
  </article>
  <div class="abs badge" style="left:40px"><svg width="100" height="100" viewBox="0 0 100 100" fill="none" stroke="#fff" stroke-width="3"><circle cx="50" cy="44" r="18"/><circle cx="50" cy="44" r="6"/><path d="M40 62v14h20V62"/></svg></div>
  <div class="abs badge" style="left:449px"><svg width="100" height="100" viewBox="0 0 100 100" fill="none" stroke="#fff" stroke-width="3"><circle cx="36" cy="40" r="8"/><circle cx="64" cy="40" r="8"/><circle cx="50" cy="48" r="9"/><path d="M24 72c2-12 22-12 24 0M52 72c2-12 22-12 24 0M36 78c2-14 26-14 28 0"/></svg></div>
  <div class="abs badge" style="left:846px"><svg width="100" height="100" viewBox="0 0 100 100" fill="none" stroke="#fff" stroke-width="3"><path d="M38 60c-8-6-10-20 0-28 8-6 20-6 26 2 8 10 4 20-4 26v8H40z"/><path d="M42 76h16"/><circle cx="52" cy="44" r="6"/></svg></div>

  <h2 class="abs value-title">Bringing the Most Value to Your ERP Implementation</h2>
  <div class="abs spine"></div>

  <div class="abs node" style="top:1468px"><svg width="60" height="60" viewBox="0 0 60 60" fill="none" stroke="#1b4f86" stroke-width="2.5"><circle cx="24" cy="24" r="10"/><circle cx="24" cy="24" r="4"/><circle cx="42" cy="40" r="8"/><circle cx="42" cy="40" r="3"/></svg></div>
  <div class="abs value-item" style="top:1474px">
    <h4>Emphasis on Process Improvement and Adoption</h4>
    <p>You want to improve processes and ensure adoption.&nbsp; We can help you do both. Brivolta evaluates current processes, identifying process streamlining opportunities along with providing process insight to the ERP implementations. This enables an ERP implementation tailored to your business resulting in increased adoption</p>
  </div>

  <div class="abs node" style="top:1690px"><svg width="60" height="60" viewBox="0 0 60 60" fill="none" stroke="#1b4f86" stroke-width="2.5"><path d="M6 44h12l14 4 18-10"/><rect x="18" y="22" width="18" height="14"/><circle cx="44" cy="16" r="7"/></svg></div>
  <div class="abs value-item" style="top:1718px">
    <h4>Bringing Down Costs with the Right Resources</h4>
    <p>If you’re looking for one resource or twenty, working on-site or remote, onshore or off, we can provide them</p>
  </div>

  <div class="abs node" style="top:1912px"><svg width="60" height="60" viewBox="0 0 60 60" fill="none" stroke="#1b4f86" stroke-width="2.5"><rect x="10" y="14" width="40" height="28"/><path d="M6 46h48"/><path d="M22 22h16v10H28l-6 4z"/></svg></div>
  <div class="abs value-item" style="top:1919px">
    <h4>Need to Add Value to Your Current Installation?</h4>
    <p>If you need help to drive the most value from a system already in production, whether it is business intelligence, Lowcode Studio applications, integrations, or new features, we can help.</p>
  </div>

  <div class="abs node" style="top:2134px"><svg width="60" height="60" viewBox="0 0 60 60" fill="none" stroke="#1b4f86" stroke-width="2.5"><rect x="8" y="10" width="44" height="32"/><path d="M30 42v8M20 50h20"/><circle cx="30" cy="26" r="7"/></svg></div>
  <div class="abs value-item" style="top:2144px">
    <h4 style="margin-bottom:2px">Not Sure What You Need?</h4>
    <p>If you sense something is wrong with your implementation but don’t know what it is, we can help.&nbsp; Our eight-point assessment starts with strategy and continues with the seven things that ensure success.</p>
  </div>

  <section class="abs platforms"></section>
  <div class="abs platforms-label">Platforms</div>
  <div class="abs partner" style="left:440px;top:2386px">Northwind<br>Ledger 365</div>
  <div class="abs partner" style="left:754px;top:2386px;font-weight:600">Meridian<br>CloudSuite</div>

  <svg class="abs" style="left:120px;top:2552px" width="110" height="104" viewBox="0 0 110 104" fill="none" stroke="#f2c31b" stroke-width="3"><path d="M30 60c-12 0-12-18 0-18 2-12 18-14 24-4 6-8 22-4 20 8 12 0 12 14 0 14z"/><path d="M40 60v30M70 60v30M20 50H6M90 50h14M54 36V10"/><circle cx="40" cy="94" r="5"/><circle cx="70" cy="94" r="5"/><circle cx="6" cy="50" r="4"/><circle cx="104" cy="50" r="4"/><circle cx="54" cy="8" r="4"/></svg>
  <div class="abs offer-title">Brivolta Offerings</div>
  <ul class="abs offer-list" style="left:280px;top:2577px"><li>Transformation Planning &amp; Support</li><li>Data &amp; Business Intelligence</li></ul>
  <ul class="abs offer-list" style="left:746px;top:2578px"><li>ERP Implementation &amp; Optimization</li><li>Integration Platforms</li></ul>

  <section class="abs contact"></section>
  <svg class="abs" style="left:158px;top:2744px" width="46" height="62" viewBox="0 0 46 62" fill="none" stroke="#fff" stroke-width="3"><path d="M23 59S4 36 4 22a19 19 0 0 1 38 0c0 14-19 37-19 37z"/><circle cx="23" cy="22" r="8"/></svg>
  <div class="abs contact-text" style="left:216px;top:2746px">410 Lakeview Commons Suite 220,<br>Minneapolis, MN 55401</div>
  <svg class="abs" style="left:662px;top:2754px" width="48" height="48" viewBox="0 0 48 48" fill="none" stroke="#fff" stroke-width="3"><path d="M10 4l8 10-5 6c3 7 8 12 15 15l6-5 10 8-6 8C20 44 4 28 2 10z"/><path d="M28 10a10 10 0 0 1 10 10M28 2a18 18 0 0 1 18 18"/></svg>
  <div class="abs contact-text" style="left:732px;top:2746px">Phone Number<br><strong>(651) 555-0142</strong></div>

  <div class="abs copyright">© 2022 Brivolta &nbsp;|&nbsp; All Rights Reserved</div>
</div>
</body>
</html>
```